Brevin Electric Ltd

Looking for a single page website and Facebook page design. I am an electrical contractor based on Vancouver Island. I do service, custom homes, residential and commercial installations. My company just started out, so I don't have any pictures of installs yet. I have 25 years experience. I would like the colors to be my logo colors black and I have a black Torvik Ridgeman that will be my vehicle which I will have a wrap for.
Updates

I just posted the contest today, not sure why the deadline is the same day.

Went on vacation/holiday

Industry/Entity Type

Electrician

Requirements
Must have
• Services provided, About me section, quote section,
Nice to have
• I am not quite sure yet, I need to see some designs first .

```html
<!DOCTYPE html>
<html lang="en">
<head>
<meta charset="utf-8">
<title>Brevin Electric Ltd — Electrical Services on Vancouver Island</title>
<link rel="stylesheet" href="https://fonts.googleapis.com/css2?family=Oswald:wght@500;600;700&family=Open+Sans:wght@400;600;700&display=swap">
<style>
  :root {
    --yellow: #f5b617;
    --yellow-deep: #e8a60c;
    --black: #0b0b0b;
    --charcoal: #1c1c1c;
    --smoke: #2e2e2e;
    --light: #e9e9e9;
    --white: #ffffff;
    --text-dim: #cfcfcf;
    --text-dark: #333333;
    --head: "Oswald", "Arial Narrow", sans-serif;
    --body: "Open Sans", Arial, sans-serif;
  }
  * { box-sizing: border-box; margin: 0; padding: 0; }
  html, body { width: 1200px; height: 2848px; overflow: hidden; }
  body { font-family: var(--body); background: var(--white); color: var(--text-dark); }
  .page { width: 1200px; height: 2848px; position: relative; }

  /* Hero */
  .hero {
    position: relative; height: 900px;
    background: radial-gradient(ellipse at 60% 40%, #4a4a4a 0%, #262626 45%, #0d0d0d 100%);
    color: var(--white); text-align: center;
  }
  .hero-photo { position: absolute; inset: 0; background: linear-gradient(180deg, rgba(0,0,0,.15), rgba(0,0,0,.55)); }
  .site-header {
    position: relative; z-index: 2; height: 92px; display: flex; align-items: center;
    padding: 0 56px; border-bottom: 1px solid rgba(255,255,255,.12);
  }
  .brand { display: flex; align-items: center; gap: 12px; font-family: var(--body); font-weight: 600; font-size: 15px; color: var(--white); }
  .brand-dot { width: 34px; height: 34px; border-radius: 50%; background: var(--yellow); }
  .main-nav { margin-left: auto; display: flex; align-items: center; gap: 34px; font-family: var(--head); font-weight: 500; font-size: 17px; letter-spacing: 1.5px; }
  .main-nav a { color: var(--white); text-decoration: none; }
  .main-nav a.is-active { background: var(--yellow); color: var(--black); padding: 6px 14px; }
  .search { width: 190px; height: 34px; border: 1px solid rgba(255,255,255,.7); display: flex; align-items: center; padding: 0 12px; font-size: 13px; color: var(--text-dim); letter-spacing: 2px; }
  .hero-content { position: relative; z-index: 2; padding-top: 230px; }
  .hero-title { font-family: var(--head); font-weight: 700; font-size: 96px; line-height: 1.05; text-transform: uppercase; letter-spacing: 1px; }
  .hero-title .accent { color: var(--yellow); }
  .hero-text { width: 760px; margin: 42px auto 0; font-size: 15px; line-height: 1.6; color: var(--text-dim); }
  .hero-text + .hero-text { margin-top: 10px; }
  .btn { display: inline-block; font-family: var(--head); font-weight: 600; letter-spacing: 1px; text-transform: uppercase; text-decoration: none; border-radius: 6px; }
  .btn-yellow { background: var(--yellow); color: var(--black); padding: 10px 30px; font-size: 16px; }
  .btn-black { background: var(--black); color: var(--white); padding: 8px 22px; font-size: 14px; }
  .hero .btn-yellow { margin-top: 40px; }
  .hero-rule { position: absolute; left: 0; right: 0; bottom: 0; height: 8px; background: var(--yellow); z-index: 3; }

  /* Services */
  .services { height: 540px; background: var(--light); display: flex; justify-content: center; align-items: center; gap: 48px; }
  .service-card {
    width: 300px; height: 420px; border-radius: 26px; background: var(--white); border: 4px solid var(--yellow);
    display: flex; flex-direction: column; overflow: hidden; box-shadow: 0 10px 24px rgba(0,0,0,.12);
  }
  .service-card.is-featured { background: var(--yellow); transform: translateY(-14px); }
  .card-head { padding: 30px 0 14px; text-align: center; }
  .card-head svg { width: 44px; height: 44px; }
  .card-title { font-family: var(--head); font-weight: 700; font-size: 24px; letter-spacing: 1.5px; color: var(--black); margin-top: 6px; }
  .card-body { margin: 8px 18px 0; padding: 18px; background: var(--white); border-radius: 14px; flex: 1; font-size: 14px; line-height: 1.65; color: var(--text-dark); }
  .card-foot { height: 86px; background: var(--yellow); display: flex; align-items: center; justify-content: center; }
  .is-featured .card-foot { background: transparent; }

  /* Why section */
  .why { height: 310px; background: var(--black); color: var(--white); text-align: center; padding-top: 38px; }
  .section-title { font-family: var(--body); font-weight: 600; font-size: 52px; }
  .why p, .estimate p { width: 1040px; margin: 18px auto 0; font-size: 14px; line-height: 1.6; color: var(--text-dim); }
  .why p + p, .estimate p + p { margin-top: 8px; }
  .why .btn-yellow, .estimate .btn-yellow { margin-top: 26px; }

  /* About */
  .about { height: 590px; display: flex; background: linear-gradient(90deg, var(--yellow-deep) 0%, var(--yellow) 45%, #3a3220 70%, #1a1a1a 100%); }
  .about-text { width: 560px; padding: 60px 40px 0 64px; color: var(--white); }
  .about-text .section-title { text-align: left; }
  .about-text p { margin-top: 20px; font-size: 15px; line-height: 1.7; }
  .about-text .btn-black { margin-top: 30px; }
  .about-gallery { flex: 1; display: grid; grid-template-columns: repeat(3, 160px); gap: 40px 36px; align-content: center; justify-content: center; }
  .gallery-photo { width: 160px; height: 160px; border-radius: 50%; border: 5px solid var(--white); background: radial-gradient(circle at 40% 35%, #b7a57a, #4d4535 75%); }

  /* Estimate */
  .estimate { height: 220px; background: var(--black); color: var(--white); text-align: center; padding-top: 34px; border-top: 6px solid var(--yellow); }

  /* Footer */
  .site-footer { height: 288px; background: var(--white); text-align: center; padding-top: 70px; }
  .footer-nav { display: flex; justify-content: center; gap: 60px; font-family: var(--head); font-weight: 500; font-size: 18px; letter-spacing: 2px; }
  .footer-nav a { color: var(--black); text-decoration: none; }
  .footer-legal { margin-top: 30px; display: flex; justify-content: center; gap: 40px; font-size: 12px; font-weight: 600; letter-spacing: 1px; color: var(--black); }
  .footer-copy { margin-top: 12px; font-size: 12px; color: #666; }
</style>
</head>
<body>
<div class="page">

  <section class="hero">
    <div class="hero-photo" role="img" aria-label="Dark close-up photo of an electrical panel with wiring"></div>
    <header class="site-header">
      <div class="brand"><span class="brand-dot"></span>Brevin Electric Ltd</div>
      <nav class="main-nav">
        <a class="is-active" href="#about">ABOUT US</a>
        <a href="#">OPPORTUNITY</a>
        <a href="#why">WHY BREVIN</a>
        <a href="#">CONTACT</a>
        <div class="search">SEARCH</div>
      </nav>
    </header>
    <div class="hero-content">
      <h1 class="hero-title">Electrical Services<br>Based on <span class="accent">Vancouver Island</span></h1>
      <p class="hero-text">Licensed electrical contractor serving homes and businesses across the island with safe, tidy and code compliant work on every job, large or small.</p>
      <p class="hero-text">Twenty five years in the trade, now under our own name.</p>
      <a class="btn btn-yellow" href="#services">Our Service</a>
    </div>
    <div class="hero-rule"></div>
  </section>

  <section class="services" id="services">
    <article class="service-card">
      <div class="card-head">
        <svg viewBox="0 0 24 24" aria-hidden="true"><path d="M12 3 2 12h3v8h5v-5h4v5h5v-8h3z" fill="#111"/></svg>
        <h2 class="card-title">RESIDENTIAL</h2>
      </div>
      <p class="card-body">Panel upgrades, new circuits, lighting and wiring for custom homes and renovations, done right the first time.</p>
      <div class="card-foot"><a class="btn btn-black" href="#">Learn More</a></div>
    </article>
    <article class="service-card is-featured">
      <div class="card-head">
        <svg viewBox="0 0 24 24" aria-hidden="true"><path d="M3 21V8l6-3v4l6-3v4l6-3v14z" fill="#111"/></svg>
        <h2 class="card-title">COMMERCIAL</h2>
      </div>
      <p class="card-body">Tenant improvements, lighting retrofits and power distribution for shops, offices and light industrial spaces.</p>
      <div class="card-foot"><a class="btn btn-black" href="#">Learn More</a></div>
    </article>
    <article class="service-card">
      <div class="card-head">
        <svg viewBox="0 0 24 24" aria-hidden="true"><circle cx="12" cy="12" r="7" fill="none" stroke="#111" stroke-width="4" stroke-dasharray="3.2 2.3"/><circle cx="12" cy="12" r="3" fill="#111"/></svg>
        <h2 class="card-title">SERVICE</h2>
      </div>
      <p class="card-body">Troubleshooting, repairs and maintenance calls with clear pricing and a tradesman who shows up on time.</p>
      <div class="card-foot"><a class="btn btn-black" href="#">Learn More</a></div>
    </article>
  </section>

  <section class="why" id="why">
    <h2 class="section-title">Why Brevin Services</h2>
    <p>Every install is planned with you, built to last and left clean. We explain the work, quote it honestly and stand behind it long after the final inspection is signed off.</p>
    <p>From a single outlet to a full commercial fit out, you get the same care and experience.</p>
    <a class="btn btn-yellow" href="#">Schedule an Estimate</a>
  </section>

  <section class="about" id="about">
    <div class="about-text">
      <h2 class="section-title">About Us</h2>
      <p>Brevin Electric Ltd was started by a journeyman electrician with twenty five years of field experience on Vancouver Island. Custom homes, residential wiring, commercial installs and service calls are all part of the daily work.</p>
      <p>You will find the truck, wrapped in company colours, parked outside job sites from Victoria to Campbell River.</p>
      <a class="btn btn-black" href="#">Learn More</a>
    </div>
    <div class="about-gallery">
      <div class="gallery-photo" role="img" aria-label="Electrician working on a breaker panel"></div>
      <div class="gallery-photo" role="img" aria-label="Hands stripping electrical wire"></div>
      <div class="gallery-photo" role="img" aria-label="Multimeter testing an outlet"></div>
      <div class="gallery-photo" role="img" aria-label="Installing a light fixture"></div>
      <div class="gallery-photo" role="img" aria-label="Coils of electrical cable"></div>
      <div class="gallery-photo" role="img" aria-label="Tools laid out on a workbench"></div>
    </div>
  </section>

  <section class="estimate">
    <p>Ready to plan your project? Tell us about the job and we will book a visit, look over the site and send a written estimate within two business days.</p>
    <p>No pressure and no surprise charges.</p>
    <a class="btn btn-yellow" href="#">Schedule an Estimate</a>
  </section>

  <footer class="site-footer">
    <nav class="footer-nav">
      <a href="#">HOME</a>
      <a href="#about">ABOUT US</a>
      <a href="#">OPPORTUNITY</a>
      <a href="#why">WHY BREVIN</a>
      <a href="#">CONTACT</a>
    </nav>
    <div class="footer-legal"><span>PRIVACY POLICY</span><span>TERMS AND CONDITIONS</span></div>
    <p class="footer-copy">© 2024 Brevin Electric Ltd | Company Reg 00000000</p>
  </footer>

</div>
</body>
</html>
```